terras letterhead

We would like to create a new letterhead that our company will use for proposals, invoices, statements and letters. Our company name is Terra-Crafters. We are a landscape design/build and landscape maintenance company. We have a web site Terra-Crafters.example where our logo (the leaf with the lettering within it only) is displayed.

Industry/Entity Type

Graphic Design

Requirements
Must have
• Address and info on our current letterhead (uploaded)
Nice to have
• We would like the design to look presentable in grey scale as well as color.
Should not have
• Do not want to infringe much on the normal useable area within the normal print areas.

```html
<!DOCTYPE html>
<html lang="en">
<head>
<meta charset="utf-8">
<title>Terra-Crafters Letterhead</title>
<link href="https://fonts.googleapis.com/css2?family=Arimo:wght@400;700&display=swap" rel="stylesheet">
<style>
  :root {
    --backdrop: #e6e4df;
    --paper: #ffffff;
    --forest: #1d4522;
    --leaf: #2f8a3c;
    --ink: #111111;
    --reverse: #ffffff;
  }
  * { box-sizing: border-box; margin: 0; padding: 0; }
  html, body {
    width: 1200px;
    height: 958px;
    overflow: hidden;
    background: var(--backdrop);
    font-family: "Arimo", Arial, sans-serif;
  }
  .letterhead {
    position: absolute;
    left: 268px;
    top: 49px;
    width: 665px;
    height: 860px;
    background: var(--paper);
    box-shadow: 0 4px 14px rgba(0,0,0,0.18);
    overflow: hidden;
  }
  .brand {
    position: absolute;
    left: 36px;
    top: 70px;
    display: flex;
    align-items: center;
    gap: 10px;
  }
  .brand-mark {
    width: 14px;
    height: 14px;
    border-radius: 50%;
    background: var(--forest);
  }
  .brand-name {
    font-size: 25px;
    font-weight: 700;
    color: var(--forest);
    letter-spacing: 0.5px;
  }
  .contact {
    position: absolute;
    right: 58px;
    top: 40px;
    text-align: center;
    color: var(--ink);
    font-size: 15px;
    line-height: 17px;
  }
  .contact .email { margin-bottom: 3px; }
  .contact .address { margin-top: 3px; margin-right: -8px; }
  .header-rule {
    position: absolute;
    left: 37px;
    right: 50px;
    top: 143px;
    height: 2px;
    background: var(--forest);
  }
  .footer-band {
    position: absolute;
    left: 0;
    bottom: 0;
    width: 665px;
    height: 74px;
  }
  .footer-url {
    position: absolute;
    left: 0;
    right: 0;
    bottom: 22px;
    text-align: center;
    color: var(--reverse);
    font-size: 16px;
    letter-spacing: 0.8px;
  }
</style>
</head>
<body>
  <main class="letterhead">
    <header>
      <div class="brand">
        <span class="brand-mark"></span>
        <span class="brand-name">Terra-Crafters</span>
      </div>
      <address class="contact" style="font-style:normal">
        <div class="email">service@terra-crafters.example</div>
        <div class="phone">(555) 010 - 1155</div>
        <div class="fax">FAX: (555) 010 - 7820</div>
        <div class="address">180 Meadowbrook Lane. Fairhaven,NJ 00000</div>
      </address>
      <div class="header-rule"></div>
    </header>
    <footer>
      <svg class="footer-band" viewBox="0 0 665 74" preserveAspectRatio="none" aria-hidden="true">
        <path d="M0 74 L0 62 Q332 -6 665 16 L665 74 Z" fill="var(--leaf)"/>
        <path d="M0 74 L0 68 Q332 2 665 24 L665 74 Z" fill="var(--forest)"/>
      </svg>
      <div class="footer-url">www.terra-crafters.example</div>
    </footer>
  </main>
</body>
</html>
```